Mexican Themed Party Invitations!

Hi,
We are wanting a Mexican themed party invititation for Dale's 40th!
We are wanting something that resembles an old Mexican postcard – like the ones you used to get in the 50’s–70's - the size would approximately be 7" by 5.5".
We would preferably like a double sided invite - The below details would be displayed on the back somewhere:
If there could also be room left somewhere on the back to attach a small magnet so that the invite can be stuck on the fridge:)
Dale's 40th
When: Saturday the 27th of July 2013 @ 7PM
Where: 48 Marlow Crescent, Coromandel Valley, SA
Bring: Yourself and cowboy drinkin’ boots
RSVP: Date, email and phone – make funny RSVP email address!
Dress: Preferably traditional Mexican or 70’s Cowboy/Girl – but tacky Sombrero’s and Ponchos are OK too!
Men: There will be a prize for the best grown (real) Mexican moustache
Music: by the Silver Cactus, Mexican Mariachi Band
Food: Supplied by……
Drinks: Bartender Trent will have the tequila shots and sangria ready to go
RSVP: by the 1st of July
Please note that we have attached some examples of pictures that we like as a bit of inspiration to give you a bit of an idea of which direction we are wanting to go in.
70's style would be good as Dale was born then.
We can't wait to see what you come up with!!!
Just for some inspration I found this image, which I love! If someone could do something like this, that would be awesome!
http://www.sales.pondvexel.com/items/r/r_mtp_lopez_card_81934.jpg
Dale's 40th insted of Juarez (or similar)

```html
<!DOCTYPE html>
<html lang="en">
<head>
<meta charset="utf-8">
<title>Dale's Fortieth – Invitation</title>
<link rel="stylesheet" href="https://fonts.googleapis.com/css2?family=Alfa+Slab+One&family=Pacifico&family=Raleway:wght@500&family=Nothing+You+Could+Do&display=swap">
<style>
  :root {
    --page: #ffffff;
    --card: #f5ecec;
    --card-edge: #e9dcdc;
    --ink: #3a3533;
    --rule: #6d6764;
    --tan: #e2a75e;
    --tan-shadow: #8a5a2c;
    --sky-deep: #2f5b8c;
    --sky-mid: #7d97bd;
    --cloud: #d9d9e4;
    --desert: #6e5a3c;
    --patch: #d8bf94;
    --faint: #c9b7b5;
  }
  * { box-sizing: border-box; margin: 0; padding: 0; }
  html, body {
    width: 1200px; height: 900px; overflow: hidden;
    background: var(--page);
  }
  .canvas { position: relative; width: 1200px; height: 900px; }

  .postcard {
    position: absolute; left: 300px; width: 600px;
    background: var(--card);
    box-shadow: 0 0 0 1px var(--card-edge);
  }

  /* Front */
  .postcard--front { top: 10px; height: 426px; padding: 10px; }
  .front__photo {
    position: absolute; inset: 10px;
    background:
      radial-gradient(ellipse 60% 45% at 45% 55%, var(--cloud) 0%, rgba(217,217,228,0) 70%),
      linear-gradient(180deg, var(--sky-deep) 0%, var(--sky-mid) 35%, var(--cloud) 60%, #a8a6a6 82%, var(--desert) 100%);
  }
  .front__welcome {
    position: absolute; top: 24px; left: 0; right: 0; text-align: center;
    font-family: "Raleway", sans-serif; font-weight: 500; font-size: 17px;
    letter-spacing: 6px; color: #ffffff;
  }
  .front__name {
    position: absolute; top: 36px; left: 40px;
    font-family: "Pacifico", cursive; font-size: 42px; line-height: 1.4;
    color: var(--tan); text-shadow: 2px 2px 0 var(--tan-shadow);
  }
  .front__title {
    position: absolute; top: 100px; left: 46px;
    font-family: "Alfa Slab One", serif; font-size: 80px; line-height: 1; letter-spacing: 2px;
    color: var(--tan); text-shadow: 3px 3px 0 var(--tan-shadow);
  }
  .front__patch {
    position: absolute; left: 448px; top: 360px; width: 130px; height: 28px;
    background: var(--patch); opacity: .9;
  }

  /* Back */
  .postcard--back { top: 456px; height: 432px; }
  .back__frame { position: absolute; inset: 8px; border: 1px solid var(--faint); }
  .back__heading { position: absolute; top: 14px; left: 30px; line-height: 1; }
  .back__heading-name {
    display: block; font-family: "Pacifico", cursive; font-weight: 400;
    font-size: 13px; line-height: 1.4; color: var(--faint);
  }
  .back__heading-title {
    display: block; font-family: "Alfa Slab One", serif; font-weight: 400; font-size: 26px;
    color: var(--tan); opacity: .85;
  }
  .back__details {
    position: absolute; top: 100px; left: 28px; width: 250px; list-style: none;
    font-family: "Nothing You Could Do", cursive; font-size: 11.5px; line-height: 14px;
    color: var(--ink);
  }
  .back__details li { margin-bottom: 22px; }
  .back__details li.tight { margin-bottom: 6px; }
  .back__divider {
    position: absolute; left: 300px; top: 50px; width: 1px; height: 340px; background: var(--rule);
  }
  .back__stamp {
    position: absolute; left: 498px; top: 28px; width: 64px; height: 82px;
    border: 1.5px solid var(--rule);
  }
  .back__address { position: absolute; left: 314px; top: 170px; width: 250px; list-style: none; }
  .back__address li {
    height: 50px; padding-top: 18px; border-bottom: 1.5px solid var(--rule);
    font-family: "Nothing You Could Do", cursive; font-size: 12px; color: var(--ink);
    white-space: nowrap;
  }
</style>
</head>
<body>
<main class="canvas">

  <section class="postcard postcard--front">
    <div class="front__photo" role="img" aria-label="Vintage photograph of a cloudy blue desert sky with a saguaro cactus"></div>
    <p class="front__welcome">WELCOME TO</p>
    <p class="front__name">Dale's</p>
    <h1 class="front__title">FORTIETH</h1>
    <div class="front__patch" role="img" aria-label="Small decorative paper label"></div>
  </section>

  <section class="postcard postcard--back">
    <div class="back__frame"></div>
    <h2 class="back__heading">
      <span class="back__heading-name">Dale's</span>
      <span class="back__heading-title">FORTIETH</span>
    </h2>
    <ul class="back__details">
      <li>Dress: Preferably traditional Mexican or 70's Cowboy/Girl – but tacky Sombrero's and Ponchos are OK too!</li>
      <li>Men: There will be a prize for the best grown (real) Mexican moustache</li>
      <li>Music: by the Silver Cactus, Mexican Mariachi Band</li>
      <li class="tight">Food: Supplied by……</li>
      <li>Drinks: Bartender Trent will have the tequila shots and sangria ready to go</li>
      <li>RSVP: by the 1st of July</li>
    </ul>
    <div class="back__divider"></div>
    <div class="back__stamp"></div>
    <ul class="back__address">
      <li>Saturday, 27th of July 2013 @ 7pm</li>
      <li>48 Marlow Crescent, Coromandel Valley, SA</li>
      <li>Bring yourself &amp; cowboy drinkin' boots</li>
      <li>RSVP: date, email and phone</li>
    </ul>
  </section>

</main>
</body>
</html>
```